Brisco & Tennant Price List for Dealers

Looking for a 4 pages total including front and back of catalog. Looking for a PDF that we can upload to a printer for production. Full color, professional looking. We have uploaded our current price list, just need to have it look a little more updated. See our website BriscoandTennant.com for more info on us, see our competitor DorvinandHale.com, see our vendors Trelvane.com, Morbrix.com, Quenlar.com, Dwip.com

Target Market(s)

automotive dealers, selling aftermarket products. Sunroofs, leather interiors, seat heaters, convertible top repairs, interior work see BriscoandTennant.com for info, also see our competitors dorvinandhale.com . See our vendors Trelvane.com, Morbrix.com, Quenlar.com, Dwip.com

Industry/Entity Type

Automotive

Font styles to use
Serif

Colors

Designer to choose colors to be used in the design.

Requirements
Must have
• Logo, phone number, fax number, web address and email address which is INFO@BRISCOANDTENNANT.COM
Nice to have
• just looking for a nice, professional price list/catalog to hand out at auto dealers who sell our product.

```html
<!DOCTYPE html>
<html lang="en">
<head>
<meta charset="utf-8">
<title>Brisco &amp; Tennant Dealer Price List</title>
<link href="https://fonts.googleapis.com/css2?family=Open+Sans:wght@300;400;600;700;800&display=swap" rel="stylesheet">
<style>
:root{
  --blue:#0b3a9e;
  --blue-light:#2e5fd0;
  --ink:#1b1b1b;
  --paper:#f2f2f2;
  --cell:#e9e9e9;
  --line:#bdbdbd;
  --dark:#333436;
  --stage:#8c8c8c;
}
*{margin:0;padding:0;box-sizing:border-box}
html,body{width:874px;height:1200px;overflow:hidden}
body{background:var(--stage);font-family:"Open Sans",sans-serif;color:var(--ink);position:relative}
.page{position:absolute;width:390px;height:550px;background:var(--paper);overflow:hidden}
.page::after{content:"";position:absolute;left:0;right:0;bottom:0;height:4px;background:linear-gradient(90deg,var(--dark) 0 154px,var(--blue) 154px 184px,#000 184px 222px,var(--dark) 222px)}
.p1{left:34px;top:34px}.p2{left:451px;top:34px}.p3{left:35px;top:614px}.p4{left:449px;top:614px}
.abs{position:absolute}
.photo{position:absolute}
.brand{position:absolute;font-weight:800;color:#111;text-align:center;line-height:1.05;letter-spacing:.5px}
.brand small{display:block;font-size:6px;font-weight:800;letter-spacing:1px;margin:3px 0}
.cover-list{left:262px;top:390px;color:var(--blue-light);font-weight:300;font-size:12px;line-height:15px;text-transform:uppercase}
.cover-list li{list-style:none;margin-bottom:4px}
.web{left:206px;top:519px;font-size:10px;display:flex;align-items:center;gap:4px}
.web b{color:var(--blue)}
.tab{position:absolute;background:var(--blue);color:#fff;font-weight:700;font-size:11.5px;display:flex;align-items:center;justify-content:center;letter-spacing:.3px}
.sub{position:absolute;color:var(--blue);font-weight:700;font-size:9px}
.heading{position:absolute;color:var(--blue);font-weight:700;font-size:10px;text-transform:uppercase}
.heading::after{content:"";display:block;width:30px;height:2px;background:#111;margin-top:1px}
.copy{position:absolute;font-size:7.2px;font-weight:600;line-height:10px}
.copy a,.copy em{color:var(--blue);font-style:normal}
.row{position:absolute;display:flex;height:15px;border:1px solid var(--line);font-size:6.6px;background:#fff}
.row .lbl{background:var(--cell);display:flex;align-items:center;padding-left:8px;border-right:1px solid var(--line)}
.row .amt{flex:1;display:flex;align-items:center;padding-left:12px;color:var(--blue);font-weight:700;font-size:8px}
.note{position:absolute;font-size:7px;font-weight:700}
.note.blue{color:var(--blue)}
.vbar{position:absolute;background:var(--blue);color:#fff;font-weight:700;font-size:9px;writing-mode:vertical-rl;transform:rotate(180deg);display:flex;align-items:center;justify-content:center}
.mv-head{position:absolute;left:39px;top:0;width:157px;height:38px;background:var(--blue);color:#fff;font-size:15px;font-weight:300;display:flex;align-items:flex-end;padding:0 0 5px 24px}
.mv-head b{font-weight:700;margin-left:4px}
.box{position:absolute;left:39px;width:311px;height:31px;border:1px solid var(--line);background:#fff;display:flex}
.box .d{width:137px;background:var(--cell);font-size:7.2px;line-height:10px;padding:5px 0 0 13px;border-right:1px solid var(--line)}
.box .v{color:var(--blue);font-weight:700;font-size:13px;display:flex;align-items:center;padding-left:19px}
.mem{position:absolute;left:39px;display:flex;height:17px;width:117px;border:1px solid var(--line);background:#fff;font-size:10px;font-weight:700}
.mem .g{width:41px;background:var(--cell);padding-left:9px;display:flex;align-items:center;border-right:1px solid var(--line)}
.mem .p{padding-left:10px;color:var(--blue);display:flex;align-items:center}
.tick{position:absolute;left:39px;font-size:9.5px;display:flex;align-items:center;gap:6px}
.tick b{color:var(--blue);font-size:12px}
.contact{position:absolute;color:#d6d6d6;font-size:7px;line-height:11px}
</style>
</head>
<body>

<!-- Page 1: cover -->
<section class="page p1">
  <div class="photo" style="left:42px;top:80px;width:157px;height:150px;background:linear-gradient(160deg,#0d2a8a,#061447)" role="img" aria-label="Panoramic sunroof seen from the cabin, blue tinted"></div>
  <div class="photo" style="left:42px;top:236px;width:61px;height:74px;background:linear-gradient(180deg,#5aa7e6,#1b4d9c)" role="img" aria-label="Woman standing through an open sunroof"></div>
  <div class="photo" style="left:106px;top:236px;width:93px;height:74px;background:linear-gradient(180deg,#8d8b88,#3a3837)" role="img" aria-label="Rear leather seats"></div>
  <div class="photo" style="left:203px;top:178px;width:152px;height:133px;background:linear-gradient(160deg,#9fc4c4,#48605f)" role="img" aria-label="Open sunroof viewed from the rear seats"></div>
  <div class="photo" style="left:106px;top:315px;width:143px;height:66px;background:linear-gradient(135deg,#3a3a3a,#0d0d0d)" role="img" aria-label="Gear shifter and centre console"></div>
  <div class="photo" style="left:253px;top:315px;width:102px;height:50px;background:linear-gradient(160deg,#1f4fc4,#0b2a80)" role="img" aria-label="Dashboard and steering wheel, blue tinted"></div>
  <div class="photo" style="left:42px;top:384px;width:207px;height:98px;background:linear-gradient(120deg,#c88a55,#6b4a35 60%,#2a2421)" role="img" aria-label="Tan leather front interior"></div>
  <div class="brand" style="left:242px;top:62px;width:116px;font-size:20px">BRISCO<small>INTERIORS &amp; TOPS · SINCE 1945</small>TENNANT</div>
  <ul class="abs cover-list"><li>Sunroofs</li><li>Leather Interiors</li><li>Safety &amp;<br>Convenience</li><li>Mobile Video</li></ul>
  <div class="abs web"><svg width="9" height="9" viewBox="0 0 10 10"><circle cx="5" cy="5" r="4.3" fill="none" stroke="#333" stroke-width="1"/><ellipse cx="5" cy="5" rx="2" ry="4.3" fill="none" stroke="#333" stroke-width=".8"/><line x1=".7" y1="5" x2="9.3" y2="5" stroke="#333" stroke-width=".8"/></svg><span>www.<b>briscoandtennant</b>.com</span></div>
</section>

<!-- Page 2: sunroofs / safety -->
<section class="page p2">
  <div class="photo" style="left:0;top:0;width:390px;height:145px;background:linear-gradient(100deg,#e23b35,#f06a5c 55%,#b22a26)" role="img" aria-label="Red car roof with an open sunroof"></div>
  <div class="tab" style="left:34px;top:157px;width:129px;height:28px">SUNROOFS</div>
  <p class="copy" style="left:34px;top:193px;width:310px">Don't go to just anyone! We have been installing <em>Sunroofs</em> Since 1973- Trust the Pros. All sunroofs come with a limited lifetime warranty.</p>
  <div class="sub" style="left:34px;top:218px">Full Feature Auto-Close SUNROOFS</div>
  <div class="row" style="left:34px;top:241px;width:140px"><div class="lbl" style="width:78px">All Cars</div><div class="amt">$995.00</div></div>
  <div class="row" style="left:202px;top:241px;width:138px"><div class="lbl" style="width:76px">Vans and SUV's</div><div class="amt">$1295.00</div></div>
  <div class="heading" style="left:34px;top:262px">Additional</div>
  <div class="row" style="left:34px;top:285px;width:306px"><div class="lbl" style="width:210px">Rerouting Overhead Air Vents add</div><div class="amt">$100.00</div></div>
  <div class="row" style="left:34px;top:303px;width:306px"><div class="lbl" style="width:210px">Vehicles with ridges on roof add</div><div class="amt">$100.00</div></div>
  <div class="row" style="left:34px;top:321px;width:306px"><div class="lbl" style="width:210px">Overhead Consoles add</div><div class="amt">$50.00</div></div>
  <div class="row" style="left:34px;top:339px;width:306px"><div class="lbl" style="width:210px">Spoiler Sunroofs-External Sliding Glass</div><div class="amt">$895.00</div></div>
  <div class="row" style="left:34px;top:357px;width:306px"><div class="lbl" style="width:210px">Spoiler Sunroofs-With Auto-Close</div><div class="amt">$995.00</div></div>
  <div class="tab" style="left:34px;top:381px;width:164px;height:29px">SAFETY &amp; CONVENIENCE</div>
  <div class="sub" style="left:34px;top:415px;font-size:9.5px">Navigation Systems</div>
  <div class="row" style="left:34px;top:438px;width:306px"><div class="lbl" style="width:183px">Factory Radio Integration</div><div class="amt">From $1195.00</div></div>
  <div class="row" style="left:34px;top:457px;width:306px"><div class="lbl" style="width:183px">Factory Look-A-like Navigation</div><div class="amt">From $1295.00</div></div>
  <div class="row" style="left:34px;top:476px;width:306px"><div class="lbl" style="width:183px">Halvard Navigation System</div><div class="amt">$1295.00</div></div>
  <div class="row" style="left:34px;top:495px;width:306px"><div class="lbl" style="width:183px">Corvane System</div><div class="amt">$1595.00</div></div>
  <div class="note blue" style="left:34px;top:517px">*Call For Pricing If Vehicle Has Steering Wheel Controls/Amplifier</div>
</section>

<!-- Page 3: rear sensing / leather -->
<section class="page p3">
  <div class="vbar" style="left:39px;top:32px;width:21px;height:118px">Rear Sensing Systems</div>
  <div class="row" style="left:65px;top:32px;width:280px"><div class="lbl" style="width:182px">Blind Spot Sensors</div><div class="amt">$695.00</div></div>
  <div class="row" style="left:65px;top:52px;width:280px"><div class="lbl" style="width:182px">Backup Sensors 2 Sensor Set</div><div class="amt">$350.00</div></div>
  <div class="row" style="left:65px;top:73px;width:280px"><div class="lbl" style="width:182px">Backup Sensors 3 Sensor Set</div><div class="amt">$500.00</div></div>
  <div class="row" style="left:65px;top:93px;width:280px"><div class="lbl" style="width:182px">Rear Camera Video System</div><div class="amt">$795.00</div></div>
  <div class="row" style="left:65px;top:114px;width:280px"><div class="lbl" style="width:182px">Rear Camera With Navigation Installation</div><div class="amt">$395.00</div></div>
  <div class="row" style="left:65px;top:134px;width:280px"><div class="lbl" style="width:182px">Rear Camera Into Auto-Dimming Mirror</div><div class="amt">$795.00*</div></div>
  <div class="note" style="left:39px;top:155px">*Optional Temperature/Compass/RoadLink Call For Pricing</div>
  <div class="sub" style="left:39px;top:173px">Advanced Rear View Mirror</div>
  <div class="row" style="left:39px;top:194px;width:281px"><div class="lbl" style="width:199px">Auto-Dimming, Compass, Outside Temperature</div><div class="amt">$695.00</div></div>
  <div class="tab" style="left:39px;top:222px;width:164px;height:29px">LEATHER INTERIORS</div>
  <p class="copy" style="left:39px;top:261px">Nothing Beats the Luxury of Leather. Backed by a 3 year/36,000 Mile Warranty!</p>
  <div class="heading" style="left:39px;top:280px">Options</div>
  <div class="row" style="left:39px;top:302px;width:186px"><div class="lbl" style="width:138px">Two Tone Color Combos add</div><div class="amt" style="padding-left:8px">$100.00</div></div>
  <div class="row" style="left:39px;top:319px;width:186px"><div class="lbl" style="width:138px">Exotics (Inserts) add</div><div class="amt" style="padding-left:8px">$150.00</div></div>
  <div class="row" style="left:39px;top:337px;width:186px"><div class="lbl" style="width:138px">Embroidery/Logo add</div><div class="amt" style="padding-left:8px">$100.00</div></div>
  <div class="row" style="left:39px;top:354px;width:186px"><div class="lbl" style="width:138px">Perforation add</div><div class="amt" style="padding-left:8px">$50.00</div></div>
  <div class="row" style="left:39px;top:372px;width:186px"><div class="lbl" style="width:138px">Overnight Shipping on 2 Row add</div><div class="amt" style="padding-left:8px">$75.00</div></div>
  <div class="row" style="left:39px;top:389px;width:186px"><div class="lbl" style="width:138px">Overnight Shipping on 3 Row add</div><div class="amt" style="padding-left:8px">$100.00</div></div>
  <div class="sub" style="left:236px;top:301px;font-size:9.5px">Leather Packages</div>
  <div class="row" style="left:236px;top:323px;width:129px"><div class="lbl" style="width:82px">Two Row Seating</div><div class="amt" style="padding-left:6px">$945.00</div></div>
  <div class="row" style="left:236px;top:342px;width:129px"><div class="lbl" style="width:82px">Three Row Seating</div><div class="amt" style="padding-left:6px">$1345.00</div></div>
  <div class="sub" style="left:39px;top:416px;font-size:9.5px">SEAT HEATING &amp; POWER LUMBAR</div>
  <div class="vbar" style="left:39px;top:438px;width:21px;height:87px">Seat Heaters</div>
  <div class="row" style="left:65px;top:438px;width:280px"><div class="lbl" style="width:208px">With Leather Package (For Pair)</div><div class="amt">$295.00</div></div>
  <div class="row" style="left:65px;top:455px;width:280px"><div class="lbl" style="width:208px">Without Leather Package (Each)</div><div class="amt">$295.00</div></div>
  <div class="row" style="left:65px;top:473px;width:280px"><div class="lbl" style="width:208px">Power Lumbar With Leather Package (For Pair)</div><div class="amt">$395.00</div></div>
  <div class="row" style="left:65px;top:490px;width:280px"><div class="lbl" style="width:208px">Without Leather Package (Each)</div><div class="amt">$425.00</div></div>
  <div class="row" style="left:65px;top:508px;width:280px"><div class="lbl" style="width:208px">Seat Heater and Cooling System Each Seat</div><div class="amt">$595.00</div></div>
</section>

<!-- Page 4: mobile video / contact -->
<section class="page p4">
  <div class="mv-head">MOBILE<b>VIDEO</b></div>
  <p class="copy" style="left:39px;top:55px;font-size:8.6px;line-height:12px">All Units Include Monitor, Wireless Remote &amp; 2 Wireless Headphones.<br>Audio Comes Through Vehicle's Stereo System.</p>
  <div class="abs" style="left:39px;top:88px;font-size:10px;font-weight:600">All-n-One Overhead Flip Down Monitor W/DVD <span style="color:var(--blue);font-weight:700;font-size:12px">$795.00</span></div>
  <div class="heading" style="left:39px;top:112px;font-size:11px">Headrest DVD Systems</div>
  <div class="box" style="top:137px"><div class="d">7" Headrest Monitors –<br>Black, Grey or Tan Leather</div><div class="v">$995 to $1195.00</div></div>
  <div class="box" style="top:174px"><div class="d">9" Headrest Monitors –<br>Black, Grey or Tan Leather</div><div class="v">$1195 to $1395.00</div></div>
  <div class="box" style="top:210px"><div class="d">Factory Match Cloth or<br>Leather DVD Headrest System</div><div class="v">$1595.00</div></div>
  <div class="abs" style="left:39px;top:253px;font-size:10.5px">SmartFit Factory Match Headrests W/Removable Tablets</div>
  <div class="mem" style="top:271px"><div class="g">8GB</div><div class="p">$1495.00</div></div>
  <div class="mem" style="top:288px"><div class="g">16GB</div><div class="p">$1695.00</div></div>
  <div class="mem" style="top:305px"><div class="g">32GB</div><div class="p">$1795.00</div></div>
  <div class="heading" style="left:39px;top:330px;font-size:12px">Options</div>
  <div class="tick" style="top:355px"><svg width="8" height="8" viewBox="0 0 8 8"><path d="M.5 4.5 3 7 7.5 .8" fill="none" stroke="var(--blue)" stroke-width="1.2"/></svg>Extra Headphone <b>$75.00</b></div>
  <div class="tick" style="top:374px"><svg width="8" height="8" viewBox="0 0 8 8"><path d="M.5 4.5 3 7 7.5 .8" fill="none" stroke="var(--blue)" stroke-width="1.2"/></svg>Power Inverter Call For Pricing</div>
  <div class="tick" style="top:391px"><svg width="8" height="8" viewBox="0 0 8 8"><path d="M.5 4.5 3 7 7.5 .8" fill="none" stroke="var(--blue)" stroke-width="1.2"/></svg>Headrest Input Into Navigation/Radio Screen Call For Pricing</div>
  <svg class="abs" style="left:0;top:420px" width="390" height="130" viewBox="0 0 390 130">
    <polygon points="0,0 132,0 178,50 390,50 390,130 0,130" fill="var(--dark)"/>
    <polygon points="132,0 145,0 191,50 178,50" fill="var(--blue)"/>
  </svg>
  <div class="brand" style="left:288px;top:410px;width:80px;font-size:12px">BRISCO<small style="font-size:4.5px;margin:1px 0">&amp;</small>TENNANT</div>
  <div class="abs" style="left:39px;top:446px;color:#fff;font-size:11.5px;font-weight:300">CONTACT <b style="font-weight:700">US</b></div>
  <div class="contact" style="left:39px;top:467px;display:flex;gap:4px"><svg width="6" height="8" viewBox="0 0 6 8"><path d="M3 8C1 5 .3 4 .3 2.8a2.7 2.7 0 0 1 5.4 0C5.7 4 5 5 3 8z" fill="#d6d6d6"/></svg><span>Brisco &amp; Tennant<br>4471-C Marlow Ave<br>Brenton, MD 20990</span></div>
  <div class="contact" style="left:39px;top:505px"><svg width="7" height="7" viewBox="0 0 8 8"><path d="M1 .5 3 .5 3.6 2.6 2.6 3.4C3.2 4.6 4.3 5.6 5.5 6.2L6.3 5.2 7.5 5.8 7.5 7.5C3.6 7.5.5 4.4 1 .5z" fill="#d6d6d6"/></svg> 301-555-0142<br><svg width="7" height="7" viewBox="0 0 8 8"><rect x="1" y="3" width="6" height="4" fill="#d6d6d6"/><rect x="2" y=".5" width="4" height="2.5" fill="none" stroke="#d6d6d6" stroke-width=".8"/></svg> 301-555-0187</div>
  <div class="contact" style="left:150px;top:505px"><svg width="7" height="6" viewBox="0 0 8 6"><rect x=".5" y=".5" width="7" height="5" fill="none" stroke="#d6d6d6" stroke-width=".8"/><path d="M.5.5 4 3.3 7.5.5" fill="none" stroke="#d6d6d6" stroke-width=".8"/></svg> info@briscoandtennant.com<br><svg width="7" height="7" viewBox="0 0 10 10"><circle cx="5" cy="5" r="4.3" fill="none" stroke="#d6d6d6"/><line x1=".7" y1="5" x2="9.3" y2="5" stroke="#d6d6d6"/></svg> www.briscoandtennant.com</div>
</section>

</body>
</html>
```